Awesome, colorful pamphlet advertising services for disabled people and supporters

My business, The Wellness Crossroads, provides nutritional counseling services to people with and without disabilities throughout the lifespan. It also offers disability consulting, body image coaching and accessible recreation consultation. I would like something representing both children and adults which ties these activities together in a happy way.

Font styles to use
Sans Serif

Colors
00AB8E
00BBA5
67D7C9
C6EFE9
E9F9F6
FFF300
FFF600
FEFA6F
FFFEC7
FFFEE8
F0912C
F2A743
F7CA91
FBE8D2
FDF5EE
E54698
E96AAD
F1A4CE
F9D9EA
FCEFF6
6B429C
8869AF
B7A5CE
E3DAEB
F3F0F8

```html
<!DOCTYPE html>
<html lang="en">
<head>
<meta charset="utf-8">
<title>The Wellness Crossroads – Pamphlet</title>
<link href="https://fonts.googleapis.com/css2?family=Mulish:wght@300;400;600;700;800&display=swap" rel="stylesheet">
<style>
:root{
  --teal:#00AB8E; --teal-2:#00BBA5; --teal-soft:#67D7C9;
  --yellow:#FFF300; --yellow-soft:#FEFA6F;
  --orange:#F0912C; --orange-2:#F2A743;
  --pink:#E54698; --pink-2:#E96AAD; --pink-soft:#F1A4CE;
  --purple:#6B429C; --purple-2:#8869AF; --purple-soft:#B7A5CE;
  --grey:#6d6e71; --text:#58595b; --stage:#e9eaec; --paper:#ffffff;
}
*{box-sizing:border-box;margin:0;padding:0}
html,body{width:1200px;height:3104px;overflow:hidden}
body{background:var(--stage);font-family:"Mulish",Arial,sans-serif;color:var(--text);position:relative}
.page{position:absolute;left:50px;width:1100px;height:734px;background:var(--paper);overflow:hidden;box-shadow:0 4px 18px rgba(0,0,0,.12)}
.page--outside{top:758px}
.page--inside{top:1612px}
.abs{position:absolute}
.bar-purple{left:0;top:0;width:200px;height:16px;background:var(--purple);border-bottom-right-radius:14px}
.site{font-size:22px;font-weight:300;color:var(--grey);letter-spacing:.3px}
.site b{font-weight:700;color:var(--purple)}
.photo{border-radius:6px}
.sq{opacity:.85;border-radius:6px}
/* outside */
.founder-photo{left:40px;top:44px;width:124px;height:124px;border-radius:50%;background:radial-gradient(circle at 50% 40%,#f3d9c6,#b98a6e 70%,#6e4e3c)}
.about{left:184px;top:54px;font-size:42px;line-height:1;font-weight:700;color:var(--purple)}
.about span{display:block;color:var(--pink)}
.founder-name{left:186px;top:150px;font-size:13px;color:var(--grey)}
.bio{left:40px;top:196px;width:470px;font-size:12.5px;line-height:1.55}
.badge{border-radius:50%;background:var(--pink)}
.badge-ring{border-radius:50%;border:6px solid var(--pink-soft);background:#fff}
.family-photo{left:214px;top:420px;width:250px;height:150px;border:5px solid var(--pink-soft);border-radius:8px;background:linear-gradient(135deg,#f7ca91,#e96aad 55%,#8869af)}
.brand-top{left:640px;top:40px;font-size:34px;font-weight:400;color:var(--grey)}
.landscape{left:600px;top:104px;width:430px;height:400px;background:linear-gradient(180deg,#8c8f9e 0%,#b79db0 30%,#d08a55 60%,#8a4c2c 100%)}
.welcome{left:550px;top:470px;width:470px;height:150px;background:var(--teal-2);border-radius:0 0 26px 0;padding:22px 34px}
.welcome p{font-size:40px;font-weight:300;color:#fff;line-height:1.05}
.welcome strong{display:block;font-size:42px;font-weight:800;color:var(--yellow)}
.bar-orange{background:var(--orange);border-top-left-radius:14px}
/* inside */
.room-photo{left:0;top:36px;width:390px;height:270px;border-radius:0 6px 6px 0;background:linear-gradient(160deg,#f4f4f2,#d5d8dc 55%,#a9a39a)}
.indiv-title{left:40px;top:440px;font-size:22px;font-weight:700;color:var(--teal-2);line-height:1.15}
.col{width:150px;font-size:11.5px;line-height:1.45}
.col h4{font-size:12.5px;color:var(--orange);font-weight:700;margin-bottom:4px}
.services{left:600px;top:36px;font-size:72px;font-weight:800;color:var(--orange);line-height:1}
.together{left:600px;top:118px;font-size:26px;font-weight:700;color:var(--purple)}
.for-orgs{left:600px;top:156px;font-size:19px;font-weight:600;color:var(--pink)}
.list{font-size:12px;line-height:1.6;width:220px}
.list li{list-style:none;padding-left:14px;position:relative}
.list li::before{content:"";position:absolute;left:0;top:7px;width:6px;height:6px;border-radius:50%;background:var(--pink)}
.h-teal{font-size:26px;font-weight:700;color:var(--teal-2)}
.box{width:150px;height:118px;border-radius:8px;color:#fff;font-size:12px;line-height:1.4;padding:12px}
.box b{display:block;font-size:13px;margin-bottom:4px}
</style>
</head>
<body>

<section class="page page--outside">
  <div class="abs bar-purple"></div>
  <div class="abs founder-photo" role="img" aria-label="Portrait photo of the founder"></div>
  <h2 class="abs about">About <span>Our Founder</span></h2>
  <p class="abs founder-name">Dana Whitfield, MS, RDN</p>
  <p class="abs bio">Dana founded The Wellness Crossroads to help people of every ability eat well, move joyfully and feel at home in their bodies. With years of experience in nutrition counseling, disability consulting and accessible recreation, she partners with children, adults, families and organizations to build practical, person-centered plans. Her approach is warm, inclusive and grounded in research, celebrating each person's strengths at every stage of life. Dana believes wellness belongs to everyone, and she works to remove barriers so that every client can thrive.</p>
  <div class="abs badge" style="left:56px;top:392px;width:118px;height:118px" role="img" aria-label="Body image coaching badge"></div>
  <div class="abs badge-ring" style="left:70px;top:528px;width:92px;height:92px" role="img" aria-label="Certification badge"></div>
  <div class="abs family-photo" role="img" aria-label="Photo of a smiling family with children"></div>
  <p class="abs site" style="left:40px;top:670px">www.wellnesscrossroads<b>.org</b></p>

  <p class="abs brand-top">Wellness Crossroads</p>
  <div class="abs photo landscape" role="img" aria-label="Landscape photo with a rainbow over a boardwalk"></div>
  <div class="abs sq" style="left:950px;top:70px;width:92px;height:92px;background:var(--pink-2)"></div>
  <div class="abs sq" style="left:1000px;top:132px;width:82px;height:82px;background:var(--purple-2)"></div>
  <div class="abs sq" style="left:985px;top:208px;width:80px;height:80px;background:var(--yellow-soft)"></div>
  <div class="abs welcome"><p>Welcome to<strong>the Wellness Crossroads!</strong></p></div>
  <p class="abs site" style="left:700px;top:660px">www.wellnesscrossroads<b>.org</b></p>
  <div class="abs bar-orange" style="left:880px;top:710px;width:220px;height:24px"></div>
</section>

<section class="page page--inside">
  <div class="abs bar-purple"></div>
  <div class="abs room-photo" role="img" aria-label="Photo of a bright, accessible living room"></div>
  <div class="abs sq" style="left:390px;top:36px;width:96px;height:96px;background:var(--purple-2)"></div>
  <div class="abs sq" style="left:436px;top:96px;width:86px;height:86px;background:var(--pink-2)"></div>
  <div class="abs sq" style="left:404px;top:170px;width:70px;height:70px;background:var(--yellow-soft)"></div>
  <h3 class="abs indiv-title">Current Services for Individuals<br>/Families/Small Groups</h3>
  <div class="abs col" style="left:40px;top:520px"><h4>Nutrition Counseling</h4>Personal meal plans and support for healthy eating habits.</div>
  <div class="abs col" style="left:210px;top:520px"><h4>Body Image Coaching</h4>Building confidence and a kind relationship with your body.</div>
  <div class="abs col" style="left:380px;top:520px"><h4>Accessible Recreation</h4>Finding fun, inclusive activities for every ability.</div>
  <p class="abs site" style="left:40px;top:676px">www.wellnesscrossroads<b>.org</b></p>

  <h2 class="abs services">Services</h2>
  <p class="abs together">Interested in Working Together?</p>
  <p class="abs for-orgs">Services for Organizations</p>
  <ul class="abs list" style="left:600px;top:196px"><li>Program accessibility reviews</li><li>Inclusive menu planning</li><li>Staff disability training</li></ul>
  <ul class="abs list" style="left:840px;top:196px"><li>Recreation access consulting</li><li>Policy and resource guidance</li><li>Wellness program design</li></ul>
  <h3 class="abs h-teal" style="left:600px;top:300px">Presentations</h3>
  <p class="abs" style="left:600px;top:338px;font-size:12px">Learn more about available topics, tailored to your organization.</p>
  <div class="abs box" style="left:600px;top:372px;background:var(--purple-2)"><b>Nutrition</b>Eating well across the lifespan for all bodies.</div>
  <div class="abs box" style="left:764px;top:372px;background:var(--orange-2)"><b>Inclusion</b>Creating welcoming spaces for people with disabilities.</div>
  <div class="abs box" style="left:928px;top:372px;background:var(--teal-2)"><b>Body Image</b>Supporting positive self-image at every age.</div>
  <h3 class="abs h-teal" style="left:600px;top:514px;font-size:24px">Future Services</h3>
  <p class="abs col" style="left:600px;top:556px">Group cooking classes adapted for diverse needs.</p>
  <p class="abs col" style="left:764px;top:556px">Online workshops for families and caregivers.</p>
  <p class="abs col" style="left:928px;top:556px">Community recreation events open to everyone.</p>
  <div class="abs bar-orange" style="left:760px;top:690px;width:340px;height:44px;padding:9px 0 0 30px">
    <span class="site" style="color:#fff;font-size:20px">www.wellnesscrossroads<b style="color:#fff">.org</b></span>
  </div>
</section>

</body>
</html>
```